Website Re-design for Kids Playhouse Business

Need current website which looks very outdated to be re-designed to look modern and contemporary, reduce clutter significantly and make it look elegant and simple.
Current website: http://www.tinyforthouse.com.au/
A website which the business owner likes, use as reference/inspiration: http://vesk.com.au/
Looking for light green palette, natural colours. "WHAT'S ON" page/link no longer required.
Updates
Industry/Entity Type
Business
Number of Pages Required
5+ page
Look and feel
Each slider illustrates characteristics of the customer's brand and the style your logo design should communicate.

```html
<!DOCTYPE html>
<html lang="en">
<head>
<meta charset="utf-8">
<title>Tiny Fort Playhouse &amp; Cafe</title>
<link href="https://fonts.googleapis.com/css2?family=Patrick+Hand&family=Lato:wght@400;700&display=swap" rel="stylesheet">
<style>
:root{
  --sky-top:#eef5e4;
  --sky-bottom:#d6e8c0;
  --grass:#9bc86a;
  --grass-light:#c3e09a;
  --grass-deep:#6f9f3e;
  --moss:#4f7d2b;
  --leaf:#6a9c3a;
  --sage:#8fb86a;
  --olive:#7c9a4a;
  --bark:#8a6a45;
  --sun:#d9a441;
  --cream:#f5f2e8;
  --paper:#fbfaf5;
  --ink:#2e3a24;
  --grey:#6b6b60;
  --line:#d5dcc8;
  --head:"Patrick Hand", cursive;
  --body:"Lato", sans-serif;
}
*{box-sizing:border-box;margin:0;padding:0}
html,body{width:1200px;height:2875px;overflow:hidden}
body{position:relative;background:#fff;font-family:var(--body);color:var(--ink)}
.abs{position:absolute}

/* header */
.sky{left:0;top:0;width:1200px;height:780px;background:linear-gradient(180deg,var(--sky-top) 0%,var(--sky-bottom) 100%)}
.brand{left:80px;top:56px;width:200px;height:88px;display:flex;flex-direction:column;justify-content:center;align-items:center;font-family:var(--head);color:var(--moss);line-height:1}
.brand .name{font-size:40px}
.brand .sub{font-size:20px;margin-top:4px}
.call{left:824px;top:22px;color:var(--grey);font-size:15px}
.call strong{display:block;color:var(--moss);font-size:28px;font-weight:400;margin-top:8px}
.follow{left:1036px;top:22px;color:var(--grey);font-size:15px}
.follow .dots{display:flex;gap:12px;margin-top:14px}
.follow .dots span{width:12px;height:12px;border-radius:50%;background:var(--leaf)}
.nav{left:349px;top:100px;display:flex;gap:3px}
.nav a{width:94px;height:67px;display:flex;flex-direction:column;align-items:center;justify-content:center;color:#fff;background:var(--sage);text-decoration:none;font-weight:700;font-size:16px;line-height:1.1;text-align:center}
.nav a small{font-weight:400;font-size:12px;opacity:.95}
.nav a.current{background:var(--moss)}

.slider{left:77px;top:169px;width:1040px;height:518px;background:var(--paper);border-radius:4px;box-shadow:0 6px 16px rgba(60,80,40,.25)}
.slide-photo{left:8px;top:8px;width:1024px;height:438px;border-radius:6px;background:linear-gradient(100deg,#e8dcb5 0%,#f1ead6 35%,#e3ecd2 60%,#c9dfae 85%,#e6d9b8 100%)}
.slide-title{right:60px;top:155px;text-align:right;font-family:var(--head);font-size:54px;line-height:1.1;color:var(--moss)}
.slide-title .warm{color:var(--bark)}
.dots-row{left:0;top:472px;width:1040px;display:flex;justify-content:center;gap:22px}
.dots-row span{width:20px;height:20px;border-radius:50%;background:var(--line)}
.dots-row span:first-child{background:var(--leaf)}

/* features */
.grass{left:0;top:740px;width:1200px;height:630px}
.sec-title{font-family:var(--head);font-weight:400;font-size:58px;text-align:center;width:1200px;left:0;color:var(--ink)}
.sec-title .hi{color:var(--moss)}
.card{top:893px;width:255px;height:351px;border-radius:10px;box-shadow:0 3px 8px rgba(50,70,30,.25);color:#fff;text-align:center}
.card .pill{margin:22px auto 0;width:218px;height:46px;border-radius:23px;background:rgba(0,0,0,.14);font-family:var(--head);font-size:26px;line-height:46px}
.card .pic{margin:12px auto 0;width:218px;height:140px;border:4px solid #fff;border-radius:4px}
.card p{font-size:15px;line-height:1.3;margin-top:18px;height:40px}
.card .more{display:block;margin:20px auto 0;width:104px;height:36px;border-radius:18px;background:#fff;font-family:var(--head);font-size:20px;line-height:36px}
.arrow{top:1040px;width:52px;height:52px;border-radius:50%;background:rgba(255,255,255,.45)}

/* welcome */
.welcome{left:0;top:1351px;width:1200px;height:361px;background:var(--cream)}
.welcome p{left:160px;top:145px;width:880px;text-align:center;color:#5a5a50;font-size:15.5px;line-height:1.33}
.btn{height:50px;border-radius:25px;color:#fff;font-size:18px;display:flex;align-items:center;justify-content:center;background:var(--moss)}

/* testimonial & contact */
.col-title{font-family:var(--head);font-weight:400;font-size:56px;line-height:1;color:var(--ink)}
.col-title .hi{color:var(--moss)}
.quote-text{left:80px;top:1860px;width:470px;color:var(--grey);font-size:14.5px;line-height:1.8}
.qmark{left:78px;top:1848px;font-family:Georgia,serif;font-size:64px;color:var(--sage);line-height:1}
.field{border:2px solid var(--line);border-radius:22px;color:#999;font-size:14px;padding-left:22px;display:flex;align-items:center;background:#fff}

/* footer */
.f-title{font-family:var(--head);font-weight:400;font-size:22px;top:2626px}
.f-title .hi{color:var(--moss)}
.f-list{top:2668px;font-size:14px;line-height:31px;color:#4a4a40;list-style:none}
.f-row{display:flex;align-items:center;gap:14px;font-size:14px;color:#4a4a40;line-height:1.35}
.bar{left:0;top:2814px;width:1200px;height:61px;background:var(--moss);color:#fff;font-size:14px;font-weight:700;display:flex;align-items:center;justify-content:center}
.bar span{color:#f0e2b0;font-family:var(--head);font-weight:400;font-size:17px;margin:0 4px}
</style>
</head>
<body>

<!-- header -->
<div class="abs sky"></div>
<div class="abs brand"><span class="name">Tiny Fort</span><span class="sub">Playhouse &amp; Cafe</span></div>
<div class="abs call">Call Today<strong>02 9555 0148</strong></div>
<div class="abs follow">Follow Us<div class="dots"><span></span><span></span></div></div>
<nav class="abs nav">
  <a class="current">Home</a>
  <a>Hours<small>&amp; Prices</small></a>
  <a>Party<small>Packages</small></a>
  <a>Vaction<small>Care</small></a>
  <a>School<small>Holiday</small></a>
  <a>Specials<small>&amp; Promotion</small></a>
  <a>Gallery</a>
  <a>Contact</a>
</nav>

<div class="abs slider">
  <div class="abs slide-photo" role="img" aria-label="Photo of a mother and toddler in party hats celebrating a birthday"></div>
  <div class="abs slide-title">
    <div>So Much <span class="warm">fun</span> For</div>
    <div class="warm">Everyone</div>
  </div>
  <div class="abs dots-row"><span></span><span></span><span></span></div>
</div>

<!-- features -->
<svg class="abs grass" viewBox="0 0 1200 630" preserveAspectRatio="none" aria-hidden="true">
  <defs><linearGradient id="g" x1="0" y1="0" x2="0" y2="1"><stop offset="0" stop-color="#c3e09a"/><stop offset="1" stop-color="#9bc86a"/></linearGradient></defs>
  <path d="M0 30 Q150 5 300 25 T600 20 T900 28 T1200 15 V585 Q1050 625 880 600 T560 605 T250 600 T0 590 Z" fill="url(#g)"/>
</svg>
<h2 class="abs sec-title" style="top:808px">Our <span class="hi">Features</span></h2>

<div class="abs arrow" style="left:12px"><svg width="52" height="52" viewBox="0 0 52 52"><path d="M30 16 L19 26 L30 36 Z" fill="#fff"/></svg></div>
<div class="abs arrow" style="left:1136px"><svg width="52" height="52" viewBox="0 0 52 52"><path d="M22 16 L33 26 L22 36 Z" fill="#fff"/></svg></div>

<div class="abs card" style="left:77px;background:var(--leaf)">
  <div class="pill">Parties</div>
  <div class="pic" role="img" aria-label="Photo of smiling children at a birthday party" style="background:linear-gradient(135deg,#d9e6c4,#efe2c6)"></div>
  <p>Perfect venue for<br>birthdays and private parties</p>
  <span class="more" style="color:var(--leaf)">More</span>
</div>
<div class="abs card" style="left:341px;background:var(--olive)">
  <div class="pill">Parties Rooms</div>
  <div class="pic" role="img" aria-label="Photo of children in a decorated party room" style="background:linear-gradient(135deg,#f1ead9,#e2d6bf)"></div>
  <p>4 kids loving<br>party rooms themes</p>
  <span class="more" style="color:var(--olive)">More</span>
</div>
<div class="abs card" style="left:604px;background:var(--moss)">
  <div class="pill">School Holidays</div>
  <div class="pic" role="img" aria-label="Photo of children playing in a tent" style="background:linear-gradient(135deg,#c7d8cf,#a9c98a)"></div>
  <p>We host school<br>holiday programs</p>
  <span class="more" style="color:var(--moss)">More</span>
</div>
<div class="abs card" style="left:868px;background:var(--bark)">
  <div class="pill">Specials &amp; Promotions</div>
  <div class="pic" role="img" aria-label="Photo of an indoor play area" style="background:linear-gradient(135deg,#e6e9dc,#d8c6a8)"></div>
  <p>Exclusive specials &amp;<br>promotions</p>
  <span class="more" style="color:var(--bark)">More</span>
</div>

<!-- welcome -->
<section class="abs welcome">
  <h2 class="abs sec-title" style="top:60px">Welcome to <span class="hi">Tiny Fort</span></h2>
  <p class="abs">Tiny Fort is an indoor Kids Play Centre and Cafe that offers both kids and adults a chance to enjoy their time, together! We pride ourselves in offering the best indoor play centre for your kids to engage in fun and learning activities in a specially created environment that is not only warm and safe but also enhances and stimulates creativity and curiosity in a child. Tiny Fort offers variety of kids party venues like our themed party rooms which are hand painted.</p>
  <div class="abs btn" style="left:516px;top:248px;width:168px">LEARN MORE</div>
</section>

<!-- testimonial -->
<h2 class="abs col-title" style="left:80px;top:1768px">Client <span class="hi">Testimonial</span></h2>
<div class="abs qmark">&#8220;</div>
<p class="abs quote-text">&nbsp;&nbsp;&nbsp;&nbsp;&nbsp;&nbsp;Had my son's birthday party there. Kinds had such a great time time I recommend this place to everyone.Staff are amazing. Food and coffee are delicious! Thank You!!!</p>
<svg class="abs" style="left:78px;top:1966px" width="476" height="30" viewBox="0 0 476 30" aria-hidden="true">
  <path d="M0 14 H86 L100 28 L114 14 H476" fill="none" stroke="#cfd6c2" stroke-width="2"/>
</svg>
<div class="abs" role="img" aria-label="Portrait photo of the reviewer" style="left:146px;top:2002px;width:70px;height:70px;border-radius:50%;border:3px solid #e2e6da;background:linear-gradient(160deg,#eef1e8,#a8b3a0)"></div>
<div class="abs" style="left:232px;top:2014px;color:var(--bark);font-weight:700;font-size:16px">Mara Quinlan</div>
<div class="abs" style="left:232px;top:2040px;color:#888;font-size:13px;font-style:italic">CEO</div>

<!-- contact -->
<h2 class="abs col-title" style="left:624px;top:1768px">Keep in <span class="hi">Touch</span></h2>
<div class="abs field" style="left:624px;top:1859px;width:246px;height:42px">Name</div>
<div class="abs field" style="left:876px;top:1859px;width:246px;height:42px">E-Mail</div>
<div class="abs field" style="left:624px;top:1905px;width:246px;height:42px">Phone</div>
<div class="abs field" style="left:876px;top:1905px;width:246px;height:42px">Subject</div>
<div class="abs field" style="left:624px;top:1953px;width:498px;height:72px;align-items:flex-start;padding-top:12px;border-radius:16px">Message</div>
<div class="abs btn" style="left:622px;top:2032px;width:168px">LEARN MORE</div>

<!-- landscape & map -->
<div class="abs" role="img" aria-label="Illustration of green rolling hills with round trees" style="left:0;top:2040px;width:1200px;height:205px;background:linear-gradient(180deg,rgba(255,255,255,0) 0%,#c3e09a 30%,#9bc86a 70%,#6f9f3e 100%);clip-path:polygon(0 40%,15% 18%,30% 30%,45% 12%,60% 28%,75% 14%,90% 26%,100% 10%,100% 100%,0 100%)"></div>
<div class="abs" role="img" aria-label="Street map showing the playhouse location" style="left:0;top:2243px;width:1200px;height:330px;background:linear-gradient(180deg,#eeede6,#e3e4da)"></div>
<svg class="abs" style="left:628px;top:2390px" width="28" height="40" viewBox="0 0 28 40" aria-hidden="true">
  <path d="M14 0 C6 0 0 6 0 14 C0 24 14 40 14 40 C14 40 28 24 28 14 C28 6 22 0 14 0Z" fill="#4f7d2b"/><circle cx="14" cy="14" r="5" fill="#fff"/>
</svg>

<!-- footer -->
<h3 class="abs f-title" style="left:80px">Usefull <span class="hi">Links</span></h3>
<ul class="abs f-list" style="left:80px">
  <li style="color:var(--ink)">About</li><li>Services</li><li>News</li><li>Terms &amp; Conditions</li>
</ul>

<h3 class="abs f-title" style="left:345px">Contact <span class="hi">Us</span></h3>
<div class="abs f-row" style="left:345px;top:2664px">
  <svg width="16" height="22" viewBox="0 0 16 22"><path d="M8 0C3.6 0 0 3.6 0 8c0 6 8 14 8 14s8-8 8-14c0-4.4-3.6-8-8-8z" fill="var(--leaf)"/><circle cx="8" cy="8" r="3" fill="#fff"/></svg>
  <span>41 Wattle Lane Ferndale<br>2196 NSW Australia</span>
</div>
<div class="abs f-row" style="left:345px;top:2722px">
  <svg width="18" height="18" viewBox="0 0 18 18"><path d="M4 1l3 4-2 2c1 2 3 4 5 5l2-2 4 3-2 4C8 17 1 10 0 4z" fill="var(--leaf)"/></svg>
  <span>02 9555 0148</span>
</div>
<div class="abs f-row" style="left:345px;top:2758px">
  <svg width="18" height="13" viewBox="0 0 18 13"><rect width="18" height="13" rx="1" fill="var(--leaf)"/><path d="M1 1l8 6 8-6" fill="none" stroke="#fff" stroke-width="1.5"/></svg>
  <span>hello@tinyforthouse.com.au</span>
</div>

<h3 class="abs f-title" style="left:608px">Follow <span class="hi">Us</span></h3>
<div class="abs f-row" style="left:608px;top:2666px"><span style="width:30px;height:30px;border-radius:50%;background:var(--leaf)"></span>Friendbook</div>
<div class="abs f-row" style="left:608px;top:2703px"><span style="width:30px;height:30px;border-radius:50%;background:var(--sage)"></span>Chirper</div>
<div class="abs f-row" style="left:608px;top:2740px"><span style="width:30px;height:30px;border-radius:50%;background:#c7d6b2"></span>Circles</div>

<div class="abs" style="left:909px;top:2608px;width:204px;height:110px;display:flex;flex-direction:column;align-items:center;justify-content:center;font-family:var(--head);color:var(--moss);line-height:1">
  <span style="font-size:40px">Tiny Fort</span><span style="font-size:20px;margin-top:4px">Playhouse &amp; Cafe</span>
</div>

<div class="abs bar">&copy; <span>Tiny Fort Playhouse &amp; Cafe</span> - 2018. All Rights Reserved</div>

</body>
</html>
```